Hydroponic Farm Needs a Business Card

We need a business card design for a hydroponic farm located on the Gulf Coast called 'Tallowbend Farms'. We grow many forms of lettuce and tomatoes along with other herbs and spices. We currently sell to farmer's markets though will soon be expanding to commercial accounts such as restaurants and grocery stores. The colors should be bright and vibrant to reflect the nature of our produce. The final design should communicate a professional, clean, yet friendly impression and able to be used both with farmer's markets and commercial accounts.

The pictures are an example of our product. The pictures do not have to be incorporated into the business card design.

Please put areas for information such as Names, Phone Number, E-mail address, and additional information.

Industry/Entity Type

Farm

```html
<!DOCTYPE html>
<html lang="en">
<head>
<meta charset="utf-8">
<title>Tallowbend Farms – Business Card</title>
<link rel="stylesheet" href="https://fonts.googleapis.com/css2?family=Bebas+Neue&family=Caveat:wght@500&family=Arimo:wght@400&display=swap">
<style>
  :root {
    --backdrop: #716d6c;
    --card: #e5e0db;
    --brand-red: #6e1a17;
    --ink: #1f1f1f;
    --green-light: #4cb849;
    --green-mid: #3fa545;
    --green-deep: #33843e;
    --tag-ink: #1d3a1e;
  }
  html, body {
    margin: 0;
    width: 1200px;
    height: 1000px;
    overflow: hidden;
    background: var(--backdrop);
  }
  .stage {
    width: 1200px;
    height: 1000px;
    display: flex;
    flex-direction: column;
    align-items: center;
    justify-content: center;
    gap: 56px;
  }
  .card {
    position: relative;
    width: 760px;
    height: 434px;
    background: var(--card);
    overflow: hidden;
    box-shadow: 0 4px 14px rgba(0,0,0,0.25);
  }
  .card-band {
    position: absolute;
    inset: 0;
    width: 100%;
    height: 100%;
  }
  .brand-name {
    position: absolute;
    left: 0; right: 0;
    top: 110px;
    margin: 0;
    text-align: center;
    font-family: "Bebas Neue", "Arial Narrow", sans-serif;
    font-size: 92px;
    letter-spacing: 2px;
    color: var(--brand-red);
    font-weight: 400;
  }
  .tagline {
    position: absolute;
    left: 0; right: 0;
    top: 300px;
    margin: 0;
    text-align: center;
    font-family: "Caveat", cursive;
    font-size: 34px;
    color: var(--tag-ink);
  }
  .contact-list {
    position: absolute;
    top: 44px;
    right: 70px;
    margin: 0;
    padding: 0;
    list-style: none;
    font-family: "Arimo", Arial, sans-serif;
    font-size: 24px;
    color: var(--ink);
  }
  .contact-list li {
    display: flex;
    align-items: center;
    gap: 10px;
    margin-bottom: 6px;
  }
  .contact-icon {
    width: 20px;
    height: 20px;
    flex: none;
  }
  .person {
    position: absolute;
    left: 70px;
    top: 196px;
    font-family: "Arimo", Arial, sans-serif;
  }
  .person-name {
    margin: 0;
    font-size: 32px;
    font-weight: 400;
    color: var(--brand-red);
  }
  .person-role {
    margin: 2px 0 0 190px;
    font-size: 18px;
    color: var(--ink);
  }
</style>
</head>
<body>
<main class="stage">

  <section class="card card-front" aria-label="Card front">
    <svg class="card-band" viewBox="0 0 760 434" preserveAspectRatio="none" aria-hidden="true">
      <path d="M0 250 C120 238 240 262 380 246 C520 232 640 252 760 240 L760 434 L0 434 Z" fill="var(--green-light)"/>
      <path d="M0 330 C160 318 300 344 440 326 C580 310 680 330 760 318 L760 434 L0 434 Z" fill="var(--green-mid)"/>
      <path d="M120 392 C280 378 440 400 600 380 C680 372 730 378 760 372 L760 434 L120 434 Z" fill="var(--green-deep)"/>
    </svg>
    <h1 class="brand-name">Tallowbend Farms</h1>
    <p class="tagline">Here we grow many forms of lettuce and tomatoes</p>
  </section>

  <section class="card card-back" aria-label="Card back">
    <svg class="card-band" viewBox="0 0 760 434" preserveAspectRatio="none" aria-hidden="true">
      <path d="M0 266 C140 254 260 276 400 260 C540 246 650 264 760 252 L760 434 L0 434 Z" fill="var(--green-light)"/>
      <path d="M0 340 C160 328 320 352 470 334 C600 320 700 338 760 328 L760 434 L0 434 Z" fill="var(--green-mid)"/>
      <path d="M180 396 C320 384 480 404 620 386 C700 378 740 384 760 380 L760 434 L180 434 Z" fill="var(--green-deep)"/>
    </svg>

    <ul class="contact-list">
      <li>
        <svg class="contact-icon" viewBox="0 0 20 20" aria-hidden="true">
          <path d="M2 8 C2 4 18 4 18 8 L15 9 L14 7 C11 6 9 6 6 7 L5 9 Z M5 10 L15 10 L17 17 L3 17 Z" fill="var(--brand-red)"/>
        </svg>
        <span>033-5550142</span>
      </li>
      <li>
        <svg class="contact-icon" viewBox="0 0 20 20" aria-hidden="true">
          <rect x="2" y="4" width="16" height="12" fill="none" stroke="var(--brand-red)" stroke-width="1.5"/>
          <path d="M2 4 L10 11 L18 4" fill="none" stroke="var(--brand-red)" stroke-width="1.5"/>
        </svg>
        <span>name@tallowbend.example</span>
      </li>
      <li>
        <svg class="contact-icon" viewBox="0 0 20 20" aria-hidden="true">
          <circle cx="10" cy="10" r="8" fill="var(--brand-red)"/>
          <path d="M2 10 H18 M10 2 V18 M4 6 H16 M4 14 H16" stroke="var(--card)" stroke-width="1"/>
          <ellipse cx="10" cy="10" rx="3.5" ry="8" fill="none" stroke="var(--card)" stroke-width="1"/>
        </svg>
        <span>www.tallowbend.example</span>
      </li>
    </ul>

    <div class="person">
      <p class="person-name">Firstname Lastname</p>
      <p class="person-role">Manager</p>
    </div>
  </section>

</main>
</body>
</html>
```